Mavro Scrub - Contact/Landing Page

I need a landing page which will essentially be the page that customers will go to from the 'website' link on GMB listing. It will provide a short overview of services which need to be selectable. a little further down can capture some contact details followed by a large Submit Now button etc...

I have some icon/logo's that can be utilised at the bottom of the page as industry type references.

Target Market(s)

End of Lease Cleaning Services

Industry/Entity Type

Cleaning Service

Colors

Designer to choose colors to be used in the design.

Requirements
Must have
• As per description
Should not have
• Colours to match my website mavroscrub.com.au

```html
<!DOCTYPE html>
<html lang="en">
<head>
<meta charset="utf-8">
<title>Mavro Scrub – End of Lease Cleaning &amp; Licensed Pest Control</title>
<link href="https://fonts.googleapis.com/css2?family=Roboto:wght@300;400;500&display=swap" rel="stylesheet">
<style>
  :root {
    --page-grey: #ececec;
    --royal-blue: #1f5fbf;
    --royal-blue-dark: #184fa8;
    --sky: #22c2e8;
    --sky-deep: #1aa8dc;
    --heading-blue: #1ea2dc;
    --pill: #e2f3fa;
    --text-grey: #7a7a7a;
    --input-text: #9a9a9a;
    --ink: #2a2a2a;
    --white: #ffffff;
    --card-blue: #29b3de;
    --social: #3b5998;
  }
  * { box-sizing: border-box; margin: 0; padding: 0; }
  html, body { width: 960px; height: 1200px; overflow: hidden; }
  body {
    position: relative;
    background: var(--page-grey);
    font-family: "Roboto", Arial, sans-serif;
    color: var(--text-grey);
  }
  .top-band {
    position: absolute; left: 0; top: 0; width: 960px; height: 330px;
    background: radial-gradient(circle at 30% 40%, var(--royal-blue), var(--royal-blue-dark));
  }
  .page {
    position: absolute; left: 138px; top: 30px; width: 684px;
    box-shadow: 0 4px 18px rgba(0,0,0,0.06);
  }
  .hero {
    position: relative; height: 300px;
    background: linear-gradient(100deg, #3ad0ef 0%, var(--sky) 45%, #1ab4e2 100%);
  }
  .brand-box {
    position: absolute; left: 283px; top: 55px; width: 118px; height: 144px;
    background: var(--white);
    display: flex; flex-direction: column; align-items: center; justify-content: center; gap: 8px;
  }
  .brand-mark { width: 26px; height: 26px; border-radius: 50%; background: var(--sky-deep); }
  .brand-name {
    font-size: 17px; font-weight: 500; color: var(--sky-deep);
    text-align: center; line-height: 1.15; text-transform: uppercase;
  }
  .hero-tagline {
    position: absolute; left: 0; right: 0; top: 245px;
    text-align: center; color: var(--white);
    font-size: 22.5px; font-weight: 500; line-height: 30px; letter-spacing: 0.1px; white-space: nowrap;
    transform: translateY(-15px);
  }
  .hero-tagline .divider { margin: 0 16px; }

  .services {
    background: var(--white); height: 311px; position: relative;
  }
  .service {
    position: absolute; top: 47px; width: 228px; text-align: center;
  }
  .service:nth-child(1) { left: 0; }
  .service:nth-child(2) { left: 228px; }
  .service:nth-child(3) { left: 456px; }
  .service-icon {
    width: 77px; height: 77px; margin: 0 auto; border-radius: 6px;
    background: #e6e6e6;
  }
  .service-title {
    margin-top: 16px; font-size: 21.5px; font-weight: 400; line-height: 26px; color: var(--heading-blue);
  }
  .service-text {
    margin-top: 10px; font-size: 10.8px; font-weight: 300; line-height: 18px; color: #6f6f6f;
  }
  .select-pill {
    margin: 10px auto 0; width: 108px; height: 36px; border-radius: 18px;
    background: var(--pill);
    display: flex; align-items: center; justify-content: center; gap: 8px;
    font-size: 14px; color: #555;
  }
  .checkbox {
    width: 11px; height: 11px; border: 1px solid #9bbfcf; border-radius: 2px; background: var(--white);
    display: flex; align-items: center; justify-content: center;
  }

  .enquiry {
    position: relative; height: 348px;
    background: linear-gradient(90deg, #8a8580 0%, #6e6b68 45%, #5a5a5a 75%, #4a4a4a 100%);
  }
  .field {
    position: absolute; left: 22px; width: 300px; height: 44px;
    background: var(--white); display: flex; align-items: center; padding-left: 17px;
    font-size: 12px; color: var(--input-text);
  }
  .contact-card {
    position: absolute; left: 363px; top: 107px; width: 300px; height: 134px;
    background: var(--card-blue);
  }
  .contact-email {
    position: absolute; left: 0; right: 0; top: 12px;
    display: flex; align-items: center; justify-content: center; gap: 10px;
    color: var(--white); font-size: 17.5px; font-weight: 400; white-space: nowrap;
  }
  .submit-button {
    position: absolute; left: 24px; top: 48px; width: 258px; height: 68px;
    background: var(--ink); color: var(--white);
    display: flex; align-items: center; justify-content: center;
    font-size: 40px; font-weight: 500;
  }

  .accreditations {
    background: var(--white); height: 97px; position: relative;
  }
  .badge { position: absolute; top: 20px; height: 50px; }
  .badge-certified { left: 19px; width: 119px; background: #111; border-radius: 4px; }
  .badge-partner { left: 175px; width: 178px; background: linear-gradient(90deg, #3b3f8f, #d8283a); }
  .badge-training { left: 388px; width: 82px; background: #1f3f9a; }
  .badge-college { left: 501px; width: 164px; background: #8dbb3a; }

  .footer-authority {
    position: absolute; left: 138px; top: 1120px; width: 94px; height: 32px;
    background: #cfcfcf; border-radius: 3px;
  }
  .footer-licence {
    position: absolute; left: 139px; top: 1159px; font-size: 8.6px; color: #6f6f6f;
  }
  .footer-copy {
    position: absolute; right: 138px; top: 1119px; font-size: 9px; color: #6f6f6f; word-spacing: 1px; white-space: pre;
  }
  .footer-social {
    position: absolute; left: 791px; top: 1138px; width: 30px; height: 30px;
    background: var(--social); border-radius: 2px;
  }
</style>
</head>
<body>
  <div class="top-band"></div>

  <main class="page">
    <header class="hero" role="img" aria-label="Technician in protective suit spraying pest treatment in a room, tinted blue">
      <div class="brand-box">
        <span class="brand-mark"></span>
        <span class="brand-name">Mavro<br>Scrub</span>
      </div>
      <h1 class="hero-tagline">END OF LEASE CLEANING<span class="divider">|</span>LICENSED PEST CONTROL</h1>
    </header>

    <section class="services">
      <div class="service">
        <div class="service-icon" role="img" aria-label="Floor plan line icon"></div>
        <h2 class="service-title">Cleaning</h2>
        <p class="service-text">All interior cleaning carried out to<br>Property management requirements.</p>
        <div class="select-pill">Select
          <span class="checkbox"><svg width="8" height="7" viewBox="0 0 8 7"><path d="M1 3.5 L3 5.5 L7 1" fill="none" stroke="#1ea2dc" stroke-width="1.5"/></svg></span>
        </div>
      </div>
      <div class="service">
        <div class="service-icon" role="img" aria-label="Rolled carpet line icon"></div>
        <h2 class="service-title">Carpet Cleaning</h2>
        <p class="service-text">Carpet stain cleaning to Australian<br>standard AS 3733 : 1995</p>
        <div class="select-pill">Select <span class="checkbox"></span></div>
      </div>
      <div class="service">
        <div class="service-icon" role="img" aria-label="Crossed-out bug line icon"></div>
        <h2 class="service-title">Pest Control</h2>
        <p class="service-text">Mandatory requirement for pets<br>on-premises</p>
        <div class="select-pill">Select <span class="checkbox"></span></div>
      </div>
    </section>

    <section class="enquiry" role="img" aria-label="Pest control technician in white protective suit and respirator treating a window">
      <div class="field" style="top:44px">First Name</div>
      <div class="field" style="top:98px">Surname</div>
      <div class="field" style="top:152px">Email</div>
      <div class="field" style="top:206px">Phone</div>
      <div class="field" style="top:260px">Suburb</div>
      <div class="contact-card">
        <div class="contact-email">
          <svg width="20" height="14" viewBox="0 0 20 14"><rect x="0.75" y="0.75" width="18.5" height="12.5" fill="none" stroke="#fff" stroke-width="1.5"/><path d="M1 1 L10 8 L19 1 M1 13 L7.5 6.5 M19 13 L12.5 6.5" fill="none" stroke="#fff" stroke-width="1.3"/></svg>
          info@mavroscrub.com.au
        </div>
        <div class="submit-button">SUBMIT</div>
      </div>
    </section>

    <section class="accreditations">
      <div class="badge badge-certified" role="img" aria-label="Certification badge"></div>
      <div class="badge badge-partner" role="img" aria-label="Equipment partner badge"></div>
      <div class="badge badge-training" role="img" aria-label="Training partner badge"></div>
      <div class="badge badge-college" role="img" aria-label="College accreditation badge"></div>
    </section>
  </main>

  <div class="footer-authority" role="img" aria-label="Environment authority badge"></div>
  <p class="footer-licence">Pest Licence : 4817305</p>
  <p class="footer-copy">©  Copyright  2021   Company Name.  All Rights Reserved.</p>
  <div class="footer-social" role="img" aria-label="Social page link"></div>
</body>
</html>
```